Flyer Design Project

Brindlewick is an IT support company based in the UKl . We protect small busineses from online criminals, malware threats, and technology failure. We do this by creating layers of protection around our clients and their business. We show them the dangers they’re exposed to and how we’ll eliminate them.

We would like to market some special promotions for our managed it services. We want a double sided leaflet , One side will focus on sign up today and get 2 months free it support. On the other we would want to talk about we will not be beaten on price, we offer pro active IT support. Content would need to be along those lines.

I have added a brochure that we have used in the past. Use for ideas.

Industry/Entity Type

Business

```html
<!DOCTYPE html>
<html lang="en">
<head>
<meta charset="utf-8">
<title>Brindlewick – Sign Up Today Flyer</title>
<link href="https://fonts.googleapis.com/css2?family=Ubuntu:wght@400;500;700&display=swap" rel="stylesheet">
<style>
  :root {
    --stage: #e4e4e4;
    --paper: #ffffff;
    --paper-shade: #ececec;
    --brand-blue: #1a9ad6;
    --brand-blue-deep: #0f7fbf;
    --brand-blue-light: #3fb1e6;
    --ink: #333333;
    --ink-soft: #444444;
    --cloud-line: #c9c9c9;
  }
  * { box-sizing: border-box; margin: 0; padding: 0; }
  html, body {
    width: 1200px; height: 888px; overflow: hidden;
    background: var(--stage);
    font-family: "Ubuntu", sans-serif;
  }
  .flyer {
    position: absolute; left: 303px; top: 24px;
    width: 594px; height: 840px;
    background: linear-gradient(180deg, var(--paper) 0%, var(--paper) 70%, var(--paper-shade) 100%);
    box-shadow: 0 6px 18px rgba(0,0,0,0.25);
    overflow: hidden;
  }
  .story-column {
    position: absolute; left: 0; top: 0; width: 309px; height: 100%;
    background: linear-gradient(180deg, var(--brand-blue-deep) 0%, var(--brand-blue) 55%, var(--brand-blue-light) 100%);
  }
  .hero-photo {
    position: absolute; left: 13px; top: 0; width: 278px; height: 332px;
    border: 3px solid rgba(255,255,255,0.55); border-top: none;
    border-radius: 0 0 14px 14px;
    background: radial-gradient(circle at 50% 35%, #4aa6d8 0%, #1f6fa6 45%, #0d3f66 100%);
  }
  .story-text {
    position: absolute; left: 14px; top: 362px; width: 282px;
    color: #fff; text-align: center;
    font-size: 19.5px; line-height: 28.3px; font-weight: 400;
  }
  .offer-column {
    position: absolute; left: 309px; top: 0; width: 285px; height: 100%;
  }
  .brand-name {
    position: absolute; left: 0; top: 74px; width: 100%;
    text-align: center; color: var(--brand-blue);
    font-size: 38px; font-weight: 500; letter-spacing: -0.5px;
  }
  .headline-box {
    position: absolute; left: 18px; top: 164px; width: 267px; height: 114px;
    background: var(--brand-blue);
    border: 3px solid #7fcaee; border-right: none;
    border-radius: 12px 0 0 12px;
    color: #fff; font-weight: 500; font-size: 21.5px; line-height: 30px;
    padding: 8px 0 0 20px;
  }
  .headline-box strong { font-size: 28px; font-weight: 700; }
  .services-title {
    position: absolute; left: 16px; top: 297px;
    font-size: 19px; color: var(--ink);
  }
  .services-list {
    position: absolute; left: 16px; top: 330px; width: 265px;
    list-style: none; font-size: 14.5px; color: var(--ink-soft);
  }
  .services-list li {
    position: relative; padding-left: 21px; line-height: 20px; margin-bottom: 7.5px;
  }
  .services-list svg { position: absolute; left: 0; top: 4px; width: 13px; height: 12px; }
  .special-offer {
    position: absolute; left: 26px; top: 634px; width: 240px; height: 58px;
    border: 2px solid var(--cloud-line); border-radius: 30px;
    display: flex; align-items: center; justify-content: center;
    font-size: 21px; color: var(--ink); letter-spacing: 0.5px;
  }
  .signup-box {
    position: absolute; left: 18px; top: 709px; width: 267px; height: 55px;
    background: var(--brand-blue);
    border: 3px solid #7fcaee; border-right: none;
    border-radius: 12px 0 0 12px;
    color: #fff; font-weight: 700; font-size: 30px;
    display: flex; align-items: center; justify-content: center;
  }
  .signup-note {
    position: absolute; left: 0; top: 772px; width: 100%;
    text-align: center; color: var(--ink); font-size: 22px; line-height: 29px;
  }
  .signup-note strong { font-weight: 700; font-size: 24px; }
</style>
</head>
<body>
  <main class="flyer">
    <section class="story-column">
      <div class="hero-photo" role="img" aria-label="Photo of a businessman's hand pointing up at a glowing cloud icon on a blue digital screen"></div>
      <p class="story-text">It’s the end of the work week and your staff is preparing to go home. One of your employees uploads a hot new song from his thumb drive (and a rootkit) on Friday afternoon. The rootkit spreads itself to all of the computers in your office.<br>Totally unaware of the damage that’s done, you come back to work on Monday to find that all of your computers are now out of commission.</p>
    </section>

    <section class="offer-column">
      <h1 class="brand-name">Brindlewick</h1>

      <div class="headline-box">Move your business to the cloud and pay as much as <strong>5x</strong> less.</div>

      <h2 class="services-title">Services:</h2>
      <ul class="services-list">
        <li><svg viewBox="0 0 13 12"><path d="M1 6.5 L4.5 10 L12 1.5" fill="none" stroke="#444" stroke-width="2"/></svg>Managed IT Support</li>
        <li><svg viewBox="0 0 13 12"><path d="M1 6.5 L4.5 10 L12 1.5" fill="none" stroke="#444" stroke-width="2"/></svg>Technology Consultation</li>
        <li><svg viewBox="0 0 13 12"><path d="M1 6.5 L4.5 10 L12 1.5" fill="none" stroke="#444" stroke-width="2"/></svg>Data Backup &amp; Disaster Recovery</li>
        <li><svg viewBox="0 0 13 12"><path d="M1 6.5 L4.5 10 L12 1.5" fill="none" stroke="#444" stroke-width="2"/></svg>Email Account Management</li>
        <li><svg viewBox="0 0 13 12"><path d="M1 6.5 L4.5 10 L12 1.5" fill="none" stroke="#444" stroke-width="2"/></svg>Software/Hardware Installation &amp; Repair</li>
        <li><svg viewBox="0 0 13 12"><path d="M1 6.5 L4.5 10 L12 1.5" fill="none" stroke="#444" stroke-width="2"/></svg>Broadband &amp; Telephony</li>
        <li><svg viewBox="0 0 13 12"><path d="M1 6.5 L4.5 10 L12 1.5" fill="none" stroke="#444" stroke-width="2"/></svg>Virus, Malware, &amp; Spyware Removal</li>
        <li><svg viewBox="0 0 13 12"><path d="M1 6.5 L4.5 10 L12 1.5" fill="none" stroke="#444" stroke-width="2"/></svg>Wireless Networking</li>
        <li><svg viewBox="0 0 13 12"><path d="M1 6.5 L4.5 10 L12 1.5" fill="none" stroke="#444" stroke-width="2"/></svg>Computer &amp; Network Security</li>
        <li><svg viewBox="0 0 13 12"><path d="M1 6.5 L4.5 10 L12 1.5" fill="none" stroke="#444" stroke-width="2"/></svg>Web Development</li>
      </ul>

      <div class="special-offer">Special Offer!</div>

      <div class="signup-box">Sign Up Today!</div>
      <p class="signup-note">and get <strong>2 months FREE</strong><br>IT support</p>
    </section>
  </main>
</body>
</html>
```